NorthPlain Bytes Yellow rose letterhead

I have a new logo for my company but in its current form it is too large to be used on letterhead or as a email signature. I need to have the designer use elements from the current logo and create something close to the original but more suited for smaller items.
Updates

I just uploaded a copy of our logo that does not have the weathered affect. Thanks

Industry/Entity Type

It Company

Requirements
Must have
• The design must maintain the visual effect of the current logo. It needs to include the yellow rose and the name of the company.
Nice to have
• It would be nice to maintain the stamp theme and incorporate my name, address, phone, email. etc.

```html
<!DOCTYPE html>
<html lang="en">
<head>
<meta charset="utf-8">
<title>NorthPlain Bytes Letterhead</title>
<link href="https://fonts.googleapis.com/css2?family=Arimo:wght@400;700&display=swap" rel="stylesheet">
<style>
  :root {
    --paper: #ffffff;
    --header-brown: #4d4440;
    --brand-teal: #35b3b6;
    --accent-gold: #f0b52c;
    --rose-yellow: #f7cf3a;
    --rose-pale: #fdf1c8;
    --ink: #3e3431;
    --tagline: #ffffff;
  }
  html, body {
    margin: 0;
    padding: 0;
    width: 848px;
    height: 1200px;
    overflow: hidden;
    background: var(--paper);
  }
  .letterhead {
    position: relative;
    width: 848px;
    height: 1200px;
    background: var(--paper);
    font-family: "Arimo", Arial, sans-serif;
    color: var(--ink);
    overflow: hidden;
  }
  .header-band {
    position: absolute;
    left: 0; top: 0;
    width: 848px; height: 102px;
    background: var(--header-brown);
  }
  .rule-gold, .rule-teal {
    position: absolute;
    left: 0;
    width: 848px;
  }
  .header-rule-gold { top: 102px; height: 4px; background: var(--accent-gold); }
  .header-rule-teal { top: 106px; height: 4px; background: var(--brand-teal); }
  .footer-rule-gold { top: 1113px; height: 5px; background: var(--accent-gold); }
  .footer-rule-teal { top: 1118px; height: 6px; background: var(--brand-teal); }

  .brand-mark {
    position: absolute;
    left: 20px; top: 22px;
    width: 140px; height: 140px;
    border-radius: 50%;
    background: var(--rose-yellow);
  }
  .brand-name {
    position: absolute;
    left: 230px; top: 20px;
    margin: 0;
    font-size: 40px;
    font-weight: 700;
    line-height: 1;
    color: var(--brand-teal);
    letter-spacing: 1.5px;
    white-space: nowrap;
  }
  .brand-tagline {
    position: absolute;
    left: 231px; top: 68px;
    margin: 0;
    font-size: 20px;
    font-weight: 400;
    line-height: 1;
    letter-spacing: 5.4px;
    color: var(--tagline);
    white-space: nowrap;
  }
  .rose-backdrop {
    position: absolute;
    left: -40px; top: 800px;
    width: 640px; height: 560px;
    border-radius: 50%;
    background: radial-gradient(ellipse at 45% 40%, var(--rose-pale) 0%, rgba(253,241,200,0.7) 45%, rgba(253,241,200,0) 72%);
  }
  .footer-contact {
    position: absolute;
    left: 0; top: 1124px;
    width: 848px; height: 76px;
    font-size: 16px;
  }
  .contact-address {
    position: absolute;
    left: 202px; top: 16px;
    white-space: nowrap;
  }
  .contact-person {
    position: absolute;
    right: 38px; top: 14px;
    font-weight: 700;
    font-size: 17px;
    white-space: nowrap;
  }
  .contact-line {
    position: absolute;
    top: 42px;
    display: flex;
    align-items: center;
    gap: 20px;
    white-space: nowrap;
  }
  .contact-email { left: 203px; }
  .contact-phone { left: 475px; }
  .contact-line svg { display: block; }
</style>
</head>
<body>
  <main class="letterhead">
    <header>
      <div class="header-band"></div>
      <div class="rule-gold header-rule-gold"></div>
      <div class="rule-teal header-rule-teal"></div>
      <div class="brand-mark" role="img" aria-label="NorthPlain Bytes brand mark"></div>
      <h1 class="brand-name">NorthPlain Bytes</h1>
      <p class="brand-tagline">SMART DATA SYSTEMS</p>
    </header>

    <div class="rose-backdrop" role="img" aria-label="Faint yellow rose watermark decoration"></div>

    <footer>
      <div class="rule-gold footer-rule-gold"></div>
      <div class="rule-teal footer-rule-teal"></div>
      <div class="footer-contact">
        <span class="contact-address">214 W Prairie Road, Ste 1108, Amber Falls, TX 75210</span>
        <span class="contact-person">Nora Whitcombe, PhD</span>
        <span class="contact-line contact-email">
          <svg width="26" height="18" viewBox="0 0 26 18" aria-hidden="true">
            <rect x="1" y="1" width="24" height="16" fill="none" stroke="#3e3431" stroke-width="1.6"/>
            <polyline points="1,1 13,10 25,1" fill="none" stroke="#3e3431" stroke-width="1.6"/>
            <line x1="1" y1="17" x2="10" y2="8" stroke="#3e3431" stroke-width="1.4"/>
            <line x1="25" y1="17" x2="16" y2="8" stroke="#3e3431" stroke-width="1.4"/>
          </svg>
          nora@northplain-bytes.com
        </span>
        <span class="contact-line contact-phone">
          <svg width="24" height="18" viewBox="0 0 24 18" aria-hidden="true">
            <path d="M1 6 C1 1 23 1 23 6 L23 8 L17 8 L17 5 L7 5 L7 8 L1 8 Z" fill="#3e3431"/>
            <path d="M6 8 L18 8 L21 17 L3 17 Z" fill="#3e3431"/>
            <circle cx="12" cy="12.5" r="2.6" fill="#ffffff"/>
          </svg>
          1-800-555-0147
        </span>
      </div>
    </footer>
  </main>
</body>
</html>
```